business card with 2 locations on 1 card

I need a modern looking business card that I would use at 2 different locations. Possibly 1 location on 1 side and other location on other side. One should be able to distinguish the 2 locations immediately before having to read the address or description on card. You can take a look at my website to see what I'm drawn to. The logo is brand new that I just purchased on Craft Hive. I want to emphasize family.
Updates

Let's not use the yellow and blue colors. Added Thursday, August 31, 2017

Target Market(s)

women and children

Industry/Entity Type

Health And Wellness

Contact Information for Business Card

Business name: Willow Brook Chiropractic & Acupuncture
My name: Lorin Daske
Job title: DC, MAOM, LAc (CA), CNS

Location 1
Address: 4817 Marlowe Blvd, Suite B-100, Frisco, TX 75034
Phone: (469) 555-0182
Fax: (972) 555-0137

Location 2
Address: 1936 Belvane Road, Suite 100, Plano, TX 75075
Phone: (469) 555-0169
Fax: (972) 555-0137

Email: drlorindaske@mailnest.example
Website: www.drlorindaske.example

Font styles to use
Serif
Sans Serif

Colors

Designer to choose colors to be used in the design.

Requirements
Must have
• distinction between 2 locations.
Nice to have
• Colors preference below is there. But I like to see what you come up with too!

```html
<!DOCTYPE html>
<html lang="en">
<head>
<meta charset="utf-8">
<title>Willow Brook Chiropractic &amp; Acupuncture – Business Card</title>
<link href="https://fonts.googleapis.com/css2?family=Cinzel:wght@600&family=Arimo:wght@400;700&display=swap" rel="stylesheet">
<style>
  :root {
    --backdrop: #1c1c1e;
    --teal: #0f6b63;
    --teal-dark: #0a554f;
    --teal-light: #1a8078;
    --leaf-green: #8ee06a;
    --name-green: #2f9e3c;
    --paper: #f6f7f6;
    --ink-grey: #5a5f5e;
    --white: #ffffff;
  }
  * { box-sizing: border-box; margin: 0; padding: 0; }
  html, body {
    width: 1200px; height: 890px; overflow: hidden;
    background: var(--backdrop);
  }
  .canvas {
    position: relative; width: 1200px; height: 890px;
    display: flex; flex-direction: column; align-items: center; justify-content: center; gap: 44px;
  }
  .card {
    position: relative; width: 630px; height: 360px; overflow: hidden;
    box-shadow: 0 12px 30px rgba(0,0,0,.45);
  }

  /* Front side */
  .card-front { display: flex; background: var(--teal); }
  .front-identity {
    width: 43%; background: var(--paper);
    display: flex; flex-direction: column; align-items: center;
    padding-top: 38px; text-align: center;
  }
  .accent-stripe { width: 7px; background: var(--leaf-green); }
  .front-locations {
    flex: 1; padding: 46px 40px 0 20px; text-align: right;
    font-family: "Arimo", sans-serif; color: var(--white);
  }
  .brand-mark {
    width: 80px; height: 80px; border-radius: 50%;
    border: 6px solid var(--teal);
  }
  .brand-name {
    font-family: "Cinzel", serif; font-weight: 600; color: var(--teal);
    font-size: 15px; line-height: 1.25; letter-spacing: .5px; margin-top: 14px;
  }
  .person-name {
    font-family: "Arimo", sans-serif; font-weight: 700; color: var(--name-green);
    font-size: 17px; margin-top: 30px; letter-spacing: .3px;
  }
  .credentials, .contact-line {
    font-family: "Arimo", sans-serif; color: var(--ink-grey); font-size: 12px;
  }
  .credentials { margin-top: 4px; }
  .contact-block { margin-top: 22px; line-height: 1.5; }
  .contact-line { font-size: 11px; }

  .office + .office { margin-top: 34px; }
  .office-title {
    font-weight: 700; color: var(--leaf-green); font-size: 15px; letter-spacing: .3px;
    display: flex; justify-content: flex-end; align-items: center; gap: 8px;
  }
  .office-title svg { width: 9px; height: 11px; }
  .office-address, .office-numbers { font-size: 14px; line-height: 1.4; }
  .office-address { margin-top: 3px; }
  .office-numbers { margin-top: 14px; }

  /* Back side */
  .card-back {
    background: linear-gradient(160deg, var(--teal-light), var(--teal) 55%, var(--teal-dark));
    display: flex; flex-direction: column; align-items: center; justify-content: center;
  }
  .leaf-texture {
    position: absolute; inset: 0;
    background: radial-gradient(ellipse at 30% 30%, rgba(255,255,255,.06), transparent 60%),
                radial-gradient(ellipse at 75% 75%, rgba(0,0,0,.08), transparent 60%);
  }
  .card-back .brand-mark {
    position: relative; width: 120px; height: 120px; border: 8px solid var(--white);
  }
  .card-back .brand-name {
    position: relative; color: var(--white); font-size: 22px; margin-top: 18px; text-align: center;
  }
</style>
</head>
<body>
<main class="canvas">
  <section class="card card-front">
    <div class="front-identity">
      <div class="brand-mark"></div>
      <p class="brand-name">Willow Brook<br>Chiropractic &amp; Acupuncture</p>
      <p class="person-name">LORIN DASKE</p>
      <p class="credentials">DC, MAOM, LAc (CA), CNS</p>
      <div class="contact-block">
        <p class="contact-line">drlorindaske@mailnest.example</p>
        <p class="contact-line">www.drlorindaske.example</p>
      </div>
    </div>
    <div class="accent-stripe"></div>
    <div class="front-locations">
      <div class="office">
        <p class="office-title">PLANO'S OFFICE:
          <svg viewBox="0 0 9 11"><path d="M8 0 L0 5.5 L8 11 Z" fill="var(--leaf-green)"/></svg></p>
        <p class="office-address">1936 Belvane Road, Suite 100<br>Plano, TX 75075</p>
        <p class="office-numbers">Phone: (469) 555-0169<br>Fax: (972) 555-0137</p>
      </div>
      <div class="office">
        <p class="office-title">FRISCO'S OFFICE:
          <svg viewBox="0 0 9 11"><path d="M8 0 L0 5.5 L8 11 Z" fill="var(--leaf-green)"/></svg></p>
        <p class="office-address">4817 Marlowe Blvd, Suite B-100<br>Frisco, TX 75034</p>
        <p class="office-numbers">Phone: (469) 555-0182<br>Fax: (972) 555-0137</p>
      </div>
    </div>
  </section>

  <section class="card card-back">
    <div class="leaf-texture" role="img" aria-label="Faint scattered leaf pattern across the teal background"></div>
    <div class="brand-mark"></div>
    <p class="brand-name">Willow Brook<br>Chiropractic &amp; Acupuncture</p>
  </section>
</main>
</body>
</html>
```